Fresh web design for high profile Golf Club

We need an exciting web site that serves both members and visitors. Our current site has the relevant sections and pages but lacks a visual impact. There are a number of very good looking golf websites out there and we want to look the best.
We need a site that will attract golfers from all over Australia to come to our course to enjoy one of the finest 36 hole championship courses as well as fantastic clubhouse facilities on their next golfing holiday.
The member section needs to provide relevant information pages and regular news and event updates to 3000 members. We are situated on the Murray River with over 300 days of sunshine and ideal golfing weather every year.
We would like to stay with our existing logo and colours as a theme.

Target Market(s)

Golfers looking for golf holiday packages.

Industry/Entity Type

Club

Requirements
Must have
• Must have contact number for golf package holidays. Must have button for member entry and button for visitor entry. Existing site is www.kelvaronegolf.com.au. Looking for a big improvement in the look of the home page.
Nice to have
• Would like constantly updated weather reporting from source such as weather channel.

```html
<!DOCTYPE html>
<html lang="en">
<head>
<meta charset="utf-8">
<title>Kelvarone Golf Club</title>
<link href="https://fonts.googleapis.com/css2?family=Signika:wght@300;400&family=Courgette&display=swap" rel="stylesheet">
<style>
:root{
  --sky:#bfeef2;
  --header-veil:rgba(236,250,250,0.82);
  --ink:#2b2b2b;
  --nav-active:#4f8a10;
  --footer-bg:#162208;
  --footer-band:rgba(20,30,8,0.78);
  --footer-text:#e6ecdc;
  --field-bg:#3a4a28;
  --field-border:#56683e;
  --btn-top:#5f9a16;
  --btn-bottom:#3f720a;
  --btn-border:#7fbf2a;
  --weather-top:#2e4a0c;
  --weather-bottom:#5d9a18;
  --social:#5f9a16;
}
*{margin:0;padding:0;box-sizing:border-box}
html,body{width:1200px;height:800px;overflow:hidden}
body{font-family:"Signika",sans-serif;background:var(--footer-bg);position:relative}
.hero{position:absolute;left:0;top:0;width:1200px;height:660px;
  background:
   linear-gradient(180deg,#cfe6ea 0%,#d7a548 18%,#c7822c 30%,#a8a8a0 42%,#6f9a38 52%,#62a62a 70%,#4e8e22 100%);}
.top-strip{position:absolute;left:0;top:0;width:1200px;height:44px;background:var(--sky)}
.header-band{position:absolute;left:0;top:44px;width:1200px;height:88px;background:var(--header-veil)}
.call{position:absolute;right:87px;top:14px;font-size:17px;color:var(--ink)}
.call small{font-size:12px}
.logo{position:absolute;left:55px;top:23px;width:272px;height:125px;background:#fff;border:1px solid #777;border-radius:10px;
  display:flex;align-items:center;gap:12px;padding-left:22px}
.logo-mark{width:58px;height:58px;border-radius:50%;background:#8dc63f;flex:none}
.logo-name{font-size:19px;letter-spacing:3px;color:#3a3a3a;font-weight:400;line-height:1.25}
.nav{position:absolute;left:357px;top:78px;display:flex;gap:0;font-size:17px;color:var(--ink)}
.nav a{color:inherit;text-decoration:none;margin-right:18px}
.nav a.active{color:var(--nav-active)}
.slide-arrow{position:absolute;top:344px;width:46px;height:46px}
.slide-arrow.prev{left:67px}.slide-arrow.next{left:1102px}
.tagline{position:absolute;left:137px;top:482px;font-family:"Courgette",cursive;font-size:24px;color:#fff;text-shadow:0 1px 3px rgba(0,0,0,.5)}
.band{position:absolute;left:0;top:625px;width:1200px;height:36px;background:var(--footer-band)}
.col-title{position:absolute;top:632px;font-size:19px;font-weight:300;color:var(--footer-text)}
.welcome-text{position:absolute;left:87px;top:672px;width:320px;font-size:15px;line-height:24px;font-weight:300;color:var(--footer-text);text-align:justify}
.field{position:absolute;top:677px;width:161px;height:28px;background:var(--field-bg);border:1px solid var(--field-border);border-radius:3px;
  color:#e8eedf;font-size:14px;padding:5px 8px;font-weight:300}
.btn{position:absolute;top:714px;height:34px;background:linear-gradient(var(--btn-top),var(--btn-bottom));border:2px solid var(--btn-border);
  border-radius:3px;color:#14240a;font-size:18px;display:flex;align-items:center;justify-content:center}
.weather{position:absolute;left:823px;top:661px;width:279px;height:87px;border-radius:0 0 6px 6px;
  background:linear-gradient(var(--weather-top),var(--weather-bottom))}
.weather svg{position:absolute;left:72px;top:12px}
.temps{position:absolute;left:138px;top:16px;font-size:19px;color:#e6ecdc;word-spacing:24px}
.day{position:absolute;left:0;width:100%;top:56px;text-align:center;font-size:21px;font-weight:300;color:#e6ecdc}
.copyright{position:absolute;left:0;width:1240px;top:777px;text-align:center;font-size:11px;color:#d8e0cc}
.social{position:absolute;top:775px;width:12px;height:12px;border-radius:50%;background:var(--social)}
</style>
</head>
<body>
<div class="hero" role="img" aria-label="Photo of a golf fairway beside a lake with autumn trees"></div>
<div class="top-strip"></div>
<div class="header-band"></div>
<div class="call"><small>Call Us :</small> 1800 555 014</div>
<div class="logo"><span class="logo-mark"></span><span class="logo-name">KELVARONE<br>GOLF CLUB</span></div>
<nav class="nav">
  <a class="active" href="#">Home</a><a href="#">Membership</a><a href="#">Golf</a><a href="#">Club House</a>
  <a href="#">News &amp; Events</a><a href="#">Golf Packages</a><a href="#">Kelvarone</a><a href="#">Gallery</a><a href="#">Contact Us</a>
</nav>
<svg class="slide-arrow prev" viewBox="0 0 46 46"><circle cx="23" cy="23" r="21" fill="#e4e4e4" stroke="#6aa620" stroke-width="2"/><path d="M28 13 L16 23 L28 33" fill="none" stroke="#333" stroke-width="3"/></svg>
<svg class="slide-arrow next" viewBox="0 0 46 46"><circle cx="23" cy="23" r="21" fill="#e4e4e4" stroke="#6aa620" stroke-width="2"/><path d="M18 13 L30 23 L18 33" fill="none" stroke="#333" stroke-width="3"/></svg>
<div class="tagline">"A great golf course is just the beginning..."</div>
<div class="band"></div>
<div class="col-title" style="left:87px">Welcome to our site</div>
<div class="col-title" style="left:450px">Members Login/ Register</div>
<div class="col-title" style="left:895px">Weather Report</div>
<p class="welcome-text">We need an exciting web site that serves both members and visitors. We need an exciting web site that serves both members and visitors.</p>
<div class="field" style="left:449px">User Name</div>
<div class="field" style="left:621px">Password</div>
<div class="btn" style="left:449px;width:80px">Login</div>
<div class="btn" style="left:537px;width:158px">Register Here</div>
<div class="weather">
  <svg width="36" height="36" viewBox="0 0 36 36"><circle cx="18" cy="18" r="11" fill="#c98a10"/><g stroke="#c98a10" stroke-width="3"><path d="M18 0v36M0 18h36M5 5l26 26M31 5L5 31"/></g></svg>
  <div class="temps">6 24</div>
  <div class="day">Tomorrow</div>
</div>
<div class="copyright">Copyright ' Kelvarone Golf Club 2012</div>
<span class="social" style="left:952px"></span>
<span class="social" style="left:980px"></span>
</body>
</html>
```